Valbrina Soletti Winery 2023 Label

We are just about to bottle our very first Napa Valley Cabernet Sauvignon and need label ideas

Target Market(s)

Cab drinkers who like Napa California Cabs

Industry/Entity Type

Wine Making

Logo Text

Valbrina Soletti 2023 Napa Estate Grown Cabernet Sauvignon

Requirements
Must have
• Winery Name, year of vintage and Napa Estate Cab
Nice to have
• If using the initials V and S use gold letters on black or red background

```html
<!DOCTYPE html>
<html lang="en">
<head>
<meta charset="utf-8">
<title>Valbrina Soletti 2023 Cabernet Sauvignon Label</title>
<link rel="stylesheet" href="https://fonts.googleapis.com/css2?family=Cinzel:wght@500&family=Oswald:wght@600&family=Syncopate:wght@400;700&display=swap">
<style>
  :root {
    --page: #ffffff;
    --label: #000000;
    --gold-dark: #8a5a22;
    --gold: #c8953f;
    --gold-light: #f0cd7a;
    --ornament: #1c1c1c;
  }
  * { margin: 0; padding: 0; box-sizing: border-box; }
  html, body { width: 1200px; height: 900px; overflow: hidden; background: var(--page); }
  .canvas { position: relative; width: 1200px; height: 900px; }
  .label {
    position: absolute; left: 351px; top: 103px; width: 500px; height: 694px;
    background: var(--label);
  }
  .rule {
    position: absolute; height: 3px;
    background: linear-gradient(90deg, var(--gold-dark), var(--gold-light) 50%, var(--gold-dark));
  }
  .rule--full { left: 0; width: 500px; }
  .rule--top { top: 65px; }
  .rule--bottom { top: 627px; }
  .rule--short { left: 76px; width: 347px; height: 2px; }
  .rule--upper { top: 469px; }
  .rule--lower { top: 543px; }
  .ornament {
    position: absolute; width: 130px; height: 200px;
    background: radial-gradient(ellipse at center, var(--ornament), rgba(28,28,28,0) 75%);
  }
  .ornament--tl { left: 17px; top: 79px; }
  .ornament--tr { left: 352px; top: 79px; }
  .ornament--bl { left: 17px; top: 414px; }
  .ornament--br { left: 352px; top: 414px; }
  .emblem { position: absolute; left: 144px; top: 109px; width: 212px; height: 212px; }
  .emblem-name {
    position: absolute; left: 0; top: 0; width: 212px; height: 212px;
    display: flex; align-items: center; justify-content: center; text-align: center;
    font-family: "Cinzel", serif; font-weight: 500; font-size: 22px; line-height: 1.15;
    color: var(--gold);
  }
  .wine-text { position: absolute; left: 0; width: 500px; text-align: center; color: var(--gold); }
  .winery-name {
    top: 348px;
    font-family: "Oswald", sans-serif; font-weight: 600; font-size: 46px; line-height: 1;
    letter-spacing: -0.5px; text-transform: uppercase;
    background: linear-gradient(90deg, var(--gold-dark), var(--gold-light) 70%, var(--gold));
    -webkit-background-clip: text; background-clip: text; color: transparent;
  }
  .vintage {
    top: 428px;
    font-family: "Syncopate", sans-serif; font-weight: 400; font-size: 25px; letter-spacing: 2px;
    color: var(--gold-light);
  }
  .designation {
    top: 490px;
    font-family: "Cinzel", serif; font-weight: 500; font-size: 30px; letter-spacing: 0.5px;
  }
  .varietal {
    top: 568px;
    font-family: "Syncopate", sans-serif; font-weight: 700; font-size: 19px; letter-spacing: 1px;
  }
</style>
</head>
<body>
<div class="canvas">
  <div class="label">
    <div class="rule rule--full rule--top"></div>

    <div class="ornament ornament--tl" role="img" aria-label="Faint scrolling floral ornament"></div>
    <div class="ornament ornament--tr" role="img" aria-label="Faint scrolling floral ornament"></div>
    <div class="ornament ornament--bl" role="img" aria-label="Faint scrolling floral ornament"></div>
    <div class="ornament ornament--br" role="img" aria-label="Faint scrolling floral ornament"></div>

    <div class="emblem">
      <svg width="212" height="212" viewBox="0 0 212 212" aria-hidden="true">
        <circle cx="106" cy="106" r="100" fill="none" stroke="#c8953f" stroke-width="4"/>
      </svg>
      <div class="emblem-name">Valbrina<br>Soletti</div>
    </div>

    <div class="wine-text winery-name">Valbrina Soletti</div>
    <div class="wine-text vintage">2023</div>
    <div class="rule rule--short rule--upper"></div>
    <div class="wine-text designation">NAPA ESTATE GROWN</div>
    <div class="rule rule--short rule--lower"></div>
    <div class="wine-text varietal">CABERNET SAUVIGNON</div>

    <div class="rule rule--full rule--bottom"></div>
  </div>
</div>
</body>
</html>
```